Business Card Design for Mabel's Pantry

We make food for dogs.
Business Card Design (using the logo designed by you). Our Brand color is a bright canary yellow. For example our signage is predominantly yellow, with the logo in black. I'd like the card also to use that imagery.
Feel free to use the two sides creatively.
Vertical Design is also great.

Industry/Entity Type

Pet food

Contact Information for Business Card

Name, email, website, phone no

Font styles to use
Sans Serif

Colors
59FF00
82FF00
B8FF75
E3FFCB
F4FFEA
FFF300
FFF600
FEFA6F
FFFEC7
FFFEE8

Requirements
Nice to have
• A graphic in the same brush stroke style of the logo shoeing a doggy bowl of food

```html
<!DOCTYPE html>
<html lang="en">
<head>
<meta charset="utf-8">
<title>Mabel's Pantry — Business Card</title>
<link rel="stylesheet" href="https://fonts.googleapis.com/css2?family=Oswald:wght@500&family=Montserrat:wght@400;500&display=swap">
<style>
  :root {
    --stage: #2a2a2c;
    --card-white: #ffffff;
    --ink: #111111;
    --band: #000000;
    --rule: #555555;
    --back-dark: #141414;
    --back-mid: #262626;
    --gold: #e8c21a;
  }
  html, body {
    margin: 0;
    padding: 0;
    width: 1200px;
    height: 1200px;
    overflow: hidden;
    background: var(--stage);
  }
  .canvas {
    position: relative;
    width: 1200px;
    height: 1200px;
  }
  .card {
    position: absolute;
    top: 250px;
    width: 420px;
    height: 700px;
    border-radius: 30px;
    overflow: hidden;
    box-shadow: 0 10px 30px rgba(0,0,0,0.35);
  }
  .card-front {
    left: 150px;
    background: var(--card-white);
    color: var(--ink);
    text-align: center;
  }
  .card-back {
    left: 630px;
  }
  .brand-name {
    position: absolute;
    top: 170px;
    left: 0;
    width: 100%;
    font-family: "Oswald", sans-serif;
    font-weight: 500;
    font-size: 46px;
    letter-spacing: 1px;
    color: var(--ink);
    margin: 0;
  }
  .name-band {
    position: absolute;
    top: 262px;
    left: 0;
    width: 100%;
    height: 92px;
    background: var(--band);
    color: var(--card-white);
  }
  .person-name {
    margin: 14px 0 0;
    font-family: "Oswald", sans-serif;
    font-weight: 500;
    font-size: 32px;
    letter-spacing: 2px;
  }
  .person-title {
    margin: 0;
    font-family: "Montserrat", sans-serif;
    font-size: 15px;
    letter-spacing: 0.5px;
  }
  .icon-row {
    position: absolute;
    top: 388px;
    left: 0;
    width: 100%;
    display: flex;
    justify-content: center;
    align-items: center;
    gap: 6px;
  }
  .icon-row .rule {
    width: 62px;
    height: 2px;
    background: var(--rule);
    margin: 0 12px;
  }
  .icon-box {
    width: 26px;
    height: 26px;
    background: var(--ink);
    border-radius: 5px;
    display: flex;
    align-items: center;
    justify-content: center;
  }
  .contact-list {
    position: absolute;
    top: 450px;
    left: 0;
    width: 100%;
    font-family: "Montserrat", sans-serif;
    font-size: 17px;
    line-height: 27px;
    margin: 0;
  }
  .divider {
    position: absolute;
    top: 572px;
    left: 138px;
    width: 144px;
    height: 2px;
    background: var(--rule);
  }
  .address {
    position: absolute;
    top: 598px;
    left: 0;
    width: 100%;
    font-family: "Montserrat", sans-serif;
    font-size: 17px;
    line-height: 27px;
    margin: 0;
  }
  .back-pattern {
    position: absolute;
    inset: 0;
    background: linear-gradient(135deg, var(--back-dark) 0%, var(--back-mid) 70%, #333 100%);
  }
  .back-brand {
    position: absolute;
    top: 332px;
    left: 0;
    width: 100%;
    text-align: center;
    font-family: "Oswald", sans-serif;
    font-weight: 500;
    font-size: 28px;
    letter-spacing: 1px;
    color: var(--gold);
    margin: 0;
  }
</style>
</head>
<body>
<div class="canvas">

  <section class="card card-front">
    <h1 class="brand-name">MABEL'S PANTRY</h1>

    <div class="name-band">
      <p class="person-name">DANA WHITFIELD</p>
      <p class="person-title">Managing Director</p>
    </div>

    <div class="icon-row">
      <span class="rule"></span>
      <span class="icon-box">
        <svg width="16" height="16" viewBox="0 0 24 24" aria-hidden="true"><path fill="#fff" d="M6.6 10.8a15.1 15.1 0 0 0 6.6 6.6l2.2-2.2a1 1 0 0 1 1-.25 11.4 11.4 0 0 0 3.6.57 1 1 0 0 1 1 1V20a1 1 0 0 1-1 1A17 17 0 0 1 3 4a1 1 0 0 1 1-1h3.5a1 1 0 0 1 1 1c0 1.25.2 2.45.57 3.57a1 1 0 0 1-.25 1z"/></svg>
      </span>
      <span class="icon-box">
        <svg width="16" height="16" viewBox="0 0 24 24" aria-hidden="true"><rect x="3" y="5" width="18" height="14" rx="2" fill="#fff"/><path d="M3.5 6l8.5 7 8.5-7" fill="none" stroke="#111" stroke-width="1.8"/></svg>
      </span>
      <span class="icon-box">
        <svg width="16" height="16" viewBox="0 0 24 24" aria-hidden="true"><g fill="none" stroke="#fff" stroke-width="1.8"><circle cx="12" cy="12" r="9"/><ellipse cx="12" cy="12" rx="4" ry="9"/><path d="M3 12h18"/></g></svg>
      </span>
      <span class="rule"></span>
    </div>

    <p class="contact-list">
      555-014-2286<br>
      info@mabelspantry.com<br>
      www.mabelspantry.com
    </p>

    <div class="divider"></div>

    <p class="address">
      18 Orchard Lane<br>
      Millbrook, NC 27000
    </p>
  </section>

  <section class="card card-back">
    <div class="back-pattern" role="img" aria-label="Repeating glossy brand mark pattern on black"></div>
    <p class="back-brand">MABEL'S PANTRY</p>
  </section>

</div>
</body>
</html>
```